Modern CNC Machining Facility in Need of Web Site Improvement

Brightmoor Fabrication and Tooling, LLC is in need of a web site update. We need to highlight both product sales and our manufacturing services offered. We have recently started offering online product sales and need a better ecommerce platform for our customers. We would like the design winner to be able to freelance the project to a fully functioning webpage.
www.brightmoorfab.example
What we like about our current web site:
Black and red highlight colors
Gear and caliper logo
USMC Veteran owned business
What we don't like about our current web site:
Unorganized
Doesn't stand out
Looks like it was made in 1995
Online Product sales are awkward

```html
<!DOCTYPE html>
<html lang="en">
<head>
<meta charset="utf-8">
<title>Brightmoor Fabrication and Tooling, LLC</title>
<link rel="stylesheet" href="https://fonts.googleapis.com/css2?family=Roboto+Condensed:wght@400;700&family=Open+Sans:wght@400;600&family=Arimo:wght@400;700&display=swap">
<style>
  :root {
    --red: #a3171a;
    --nav-red: #a8181b;
    --ink: #1d1d1d;
    --text: #333333;
    --page: #f1f1f1;
    --band: #dcdcdc;
    --card: #ffffff;
    --button: #262626;
    --footer: #161616;
    --footer-field: #222222;
    --footer-line: #3a3a3a;
    --wood-light: #edd6bd;
    --wood-mid: #e2c4a4;
    --photo-a: #8a8f93;
    --photo-b: #4a4e52;
    --overlay: rgba(110, 110, 110, 0.8);
  }
  * { box-sizing: border-box; margin: 0; padding: 0; }
  html, body { width: 810px; height: 1200px; overflow: hidden; }
  body { background: var(--page); font-family: "Arimo", Arial, sans-serif; color: var(--text); }
  .page { position: relative; width: 810px; height: 1200px; overflow: hidden; }
  .wrap { width: 588px; margin: 0 auto; position: relative; }

  /* Header */
  .site-header { height: 75px; background: #f6f6f6; }
  .site-header .wrap { height: 75px; display: flex; align-items: center; }
  .brand { display: flex; align-items: center; gap: 10px; }
  .brand-mark { width: 62px; height: 62px; border-radius: 50%; background: var(--red); flex: none; }
  .brand-name { font-family: "Roboto Condensed", sans-serif; font-weight: 700; font-size: 11.5px; color: var(--ink); line-height: 1.15; white-space: nowrap; text-transform: uppercase; }
  .brand-tag { font-family: "Roboto Condensed", sans-serif; font-size: 8px; color: var(--ink); text-transform: uppercase; margin-top: 4px; line-height: 1.2; }
  .search { margin-left: auto; width: 131px; height: 20px; background: #fff; border: 1px solid #d6d6d6; border-bottom: 2px solid #bdbdbd; border-radius: 2px; display: flex; align-items: center; justify-content: space-between; padding: 0 8px; font-size: 9px; color: #999; }
  .social { display: flex; gap: 4px; margin-left: 18px; }
  .social span { width: 19px; height: 19px; border-radius: 50%; background: var(--red); display: block; }

  /* Navigation */
  .main-nav { height: 32px; background: var(--nav-red); border-top: 1px solid #7a0f11; border-bottom: 1px solid #7a0f11; }
  .main-nav ul { list-style: none; display: flex; height: 30px; }
  .main-nav li { font-size: 10.5px; color: #fff; padding: 0 10px; line-height: 30px; margin-right: 8px; }
  .main-nav li.is-active { background: #0f0f0f; }

  /* Hero */
  .hero { position: relative; height: 250px; }
  .hero-backdrop { position: absolute; inset: 0; background: linear-gradient(90deg, var(--wood-light), var(--wood-mid) 50%, var(--wood-light)); }
  .hero-arrow { position: absolute; top: 105px; }
  .hero-arrow.prev { left: 8px; }
  .hero-arrow.next { right: 8px; }
  .hero-title { position: absolute; left: 116px; top: 87px; background: var(--overlay); color: #1a1a1a; font-family: "Open Sans", sans-serif; font-weight: 600; font-size: 17px; line-height: 40px; height: 40px; padding: 0 14px; white-space: nowrap; }
  .hero-sub { position: absolute; left: 116px; top: 147px; background: var(--overlay); color: #1a1a1a; font-family: "Open Sans", sans-serif; font-weight: 600; font-size: 11px; line-height: 26px; height: 26px; padding: 0 11px; white-space: nowrap; }
  .hero-photo { position: absolute; left: 401px; top: 19px; width: 285px; height: 215px; border: 2px solid #b89a7a; background: linear-gradient(160deg, var(--photo-a), var(--photo-b)); }

  /* Section headings */
  .section-title { font-family: "Roboto Condensed", sans-serif; font-weight: 700; font-size: 19px; color: var(--red); text-align: center; text-transform: uppercase; }
  .section-title::after { content: ""; display: block; width: 110px; height: 2px; background: #c4c4c4; margin: 4px auto 0; }

  /* About */
  .about { height: 124px; padding-top: 16px; }
  .about p { width: 560px; margin: 14px auto 0; font-family: "Open Sans", sans-serif; font-size: 9.1px; line-height: 13.4px; text-align: center; color: var(--text); }

  /* Products */
  .products { height: 323px; background: var(--band); padding-top: 24px; }
  .product-grid { display: flex; justify-content: space-between; margin-top: 22px; }
  .product-card { width: 132px; text-align: center; }
  .product-name { background: var(--red); color: #fff; font-family: "Roboto Condensed", sans-serif; font-weight: 700; font-size: 11px; height: 25px; line-height: 25px; }
  .product-photo { height: 93px; background: linear-gradient(160deg, var(--photo-a), var(--photo-b)); }
  .product-text { font-size: 8px; line-height: 13px; color: #111; margin-top: 17px; padding: 0 10px; }
  .product-price { font-size: 15px; color: var(--red); margin-top: 10px; }
  .add-to-cart { display: inline-block; margin-top: 7px; width: 74px; height: 24px; line-height: 24px; background: var(--button); color: #fff; font-size: 9.5px; }

  /* Services & news */
  .info { height: 213px; padding-top: 46px; }
  .info .wrap { display: flex; justify-content: space-between; }
  .panel { background: var(--card); border-bottom: 1px solid var(--red); height: 129px; padding: 12px 15px; }
  .services { width: 376px; }
  .news { width: 186px; padding: 12px 10px; }
  .panel-title { font-family: "Roboto Condensed", sans-serif; font-weight: 700; font-size: 17px; color: var(--red); text-transform: uppercase; }
  .service-list { display: grid; grid-template-columns: 163px 163px; margin-top: 14px; list-style: none; }
  .service-list li { font-size: 9px; color: #333; line-height: 21px; display: flex; align-items: center; gap: 8px; }
  .service-list li::before { content: ""; width: 5px; height: 5px; border: 1px solid #444; flex: none; }
  .news-head { display: flex; justify-content: space-between; align-items: center; }
  .news-arrows { display: flex; gap: 2px; }
  .news-arrows span { width: 11px; height: 9px; background: #ccc; display: flex; align-items: center; justify-content: center; }
  .news-date { font-family: "Open Sans", sans-serif; font-size: 14px; color: #222; margin-top: 8px; padding-bottom: 4px; border-bottom: 1px solid #8aa; }
  .news-head-line { font-size: 9px; color: #111; margin-top: 10px; }
  .news-body { font-size: 7.6px; color: #555; margin-top: 6px; line-height: 11px; width: 150px; }

  /* Footer */
  .site-footer { height: 183px; background: var(--footer); color: #fff; padding-top: 24px; }
  .site-footer .wrap { display: flex; }
  .footer-col h3 { font-size: 9px; font-weight: 400; text-transform: uppercase; margin-bottom: 10px; }
  .footer-links { width: 202px; }
  .footer-links ul { list-style: none; }
  .footer-links li { font-size: 8px; line-height: 15px; }
  .footer-contact { width: 198px; }
  .field { width: 132px; height: 20px; background: var(--footer-field); border: 1px solid var(--footer-line); font-size: 8px; padding: 4px 5px; margin-bottom: 3px; }
  .field.comments { height: 49px; }
  .submit { width: 60px; height: 19px; background: #000; font-size: 8px; text-align: center; line-height: 19px; margin-top: 5px; }
  .footer-address p { font-size: 7.4px; line-height: 10px; color: #ccc; }
  .footer-address .address-text { width: 110px; }
  .footer-address .line { margin-top: 6px; }
  .copyright { font-size: 7.4px; color: #ccc; margin-top: 36px; white-space: nowrap; }
</style>
</head>
<body>
<div class="page">

  <header class="site-header">
    <div class="wrap">
      <div class="brand">
        <span class="brand-mark"></span>
        <div>
          <div class="brand-name">Brightmoor Fabrication and Tooling, LLC</div>
          <div class="brand-tag">CNC milling &amp; turning, production machining,<br>ice fishing spears</div>
        </div>
      </div>
      <div class="search">
        <span>Search...</span>
        <svg width="9" height="9" viewBox="0 0 10 10"><circle cx="4" cy="4" r="3" fill="none" stroke="#999" stroke-width="1.3"/><line x1="6.2" y1="6.2" x2="9.3" y2="9.3" stroke="#999" stroke-width="1.5"/></svg>
      </div>
      <div class="social" aria-label="Social links">
        <span></span><span></span><span></span><span></span>
      </div>
    </div>
  </header>

  <nav class="main-nav">
    <div class="wrap">
      <ul>
        <li class="is-active">Home</li>
        <li>Online Product Sales</li>
        <li>Ice Flashing Spears</li>
        <li>Equipment</li>
        <li>Contact-Us</li>
        <li>Brightmoor Blog</li>
      </ul>
    </div>
  </nav>

  <section class="hero">
    <div class="hero-backdrop" role="img" aria-label="Light wooden plank backdrop"></div>
    <svg class="hero-arrow prev" width="18" height="40" viewBox="0 0 18 40"><polyline points="15,2 3,20 15,38" fill="none" stroke="#8c8c8c" stroke-width="3"/></svg>
    <svg class="hero-arrow next" width="18" height="40" viewBox="0 0 18 40"><polyline points="3,2 15,20 3,38" fill="none" stroke="#8c8c8c" stroke-width="3"/></svg>
    <div class="hero-title">LOREM IPSUME DOLOR SIT</div>
    <div class="hero-sub">LOREM IPSUME DOLOR SIT</div>
    <div class="hero-photo" role="img" aria-label="Photo of a CNC plasma cutting table in the shop"></div>
  </section>

  <section class="about">
    <h2 class="section-title">About Us</h2>
    <p>Lorem Ipsum is simply dummy text of the printing and typesetting industry. Lorem Ipsum has been the industry's standard dummy text ever since the 1500s, when an unknown printer took a galley of type and scrambled it to make a type specimen book. It has survived not only five centuries, but also the leap into electronic typesetting, remaining essentially unchanged.</p>
  </section>

  <section class="products">
    <h2 class="section-title">Our Product</h2>
    <div class="wrap product-grid">
      <article class="product-card">
        <div class="product-name">Product Name</div>
        <div class="product-photo" role="img" aria-label="Product photo of a CNC cutting table"></div>
        <p class="product-text">Lorem Ipsum is simply dummy text of the printing and</p>
        <div class="product-price">$ 150.00</div>
        <span class="add-to-cart">ADD TO CART</span>
      </article>
      <article class="product-card">
        <div class="product-name">Product Name</div>
        <div class="product-photo" role="img" aria-label="Product photo of a CNC cutting table"></div>
        <p class="product-text">Lorem Ipsum is simply dummy text of the printing and</p>
        <div class="product-price">$ 150.00</div>
        <span class="add-to-cart">ADD TO CART</span>
      </article>
      <article class="product-card">
        <div class="product-name">Product Name</div>
        <div class="product-photo" role="img" aria-label="Product photo of a CNC cutting table"></div>
        <p class="product-text">Lorem Ipsum is simply dummy text of the printing and</p>
        <div class="product-price">$ 150.00</div>
        <span class="add-to-cart">ADD TO CART</span>
      </article>
      <article class="product-card">
        <div class="product-name">Product Name</div>
        <div class="product-photo" role="img" aria-label="Product photo of a CNC cutting table"></div>
        <p class="product-text">Lorem Ipsum is simply dummy text of the printing and</p>
        <div class="product-price">$ 150.00</div>
        <span class="add-to-cart">ADD TO CART</span>
      </article>
    </div>
  </section>

  <section class="info">
    <div class="wrap">
      <div class="panel services">
        <h2 class="panel-title">Our Services</h2>
        <ul class="service-list">
          <li>Lorem Ipsum is simply dummy</li>
          <li>Lorem Ipsum is simply dummy</li>
          <li>text of the printing and</li>
          <li>text of the printing and</li>
          <li>typesetting industry.</li>
          <li>typesetting industry.</li>
        </ul>
      </div>
      <div class="panel news">
        <div class="news-head">
          <h2 class="panel-title">Latest News</h2>
          <div class="news-arrows">
            <span><svg width="7" height="5" viewBox="0 0 7 5"><polyline points="3,0.5 1,2.5 3,4.5" fill="none" stroke="#333"/><line x1="1" y1="2.5" x2="7" y2="2.5" stroke="#333"/></svg></span>
            <span><svg width="7" height="5" viewBox="0 0 7 5"><polyline points="4,0.5 6,2.5 4,4.5" fill="none" stroke="#333"/><line x1="0" y1="2.5" x2="6" y2="2.5" stroke="#333"/></svg></span>
          </div>
        </div>
        <div class="news-date">12 Jan 2013</div>
        <div class="news-head-line">Lorem Ipsum has been the industry's</div>
        <p class="news-body">Lorem Ipsum is simply dummy text of the printing and typesetting industry.</p>
      </div>
    </div>
  </section>

  <footer class="site-footer">
    <div class="wrap">
      <div class="footer-col footer-links">
        <h3>Quick Link</h3>
        <ul>
          <li>Home</li>
          <li>Online Product Sales</li>
          <li>Ice Flashing Spears</li>
          <li>Equipment</li>
          <li>Contact-Us</li>
          <li>Blog</li>
        </ul>
      </div>
      <div class="footer-col footer-contact">
        <h3>Quick Contact</h3>
        <div class="field">Email</div>
        <div class="field">Phone</div>
        <div class="field comments">Comments</div>
        <div class="submit">SUBMIT</div>
      </div>
      <div class="footer-col footer-address">
        <h3>Our Address</h3>
        <p class="address-text">Lorem Ipsum has been the industry's standard dummy text ever since the</p>
        <p class="line">+1 555 014 2880</p>
        <p class="line">info@brightmoorfab.example</p>
        <p class="copyright">Copyright &copy; 2014. All right reserved.</p>
      </div>
    </div>
  </footer>

</div>
</body>
</html>
```